Shopify Page integration

As agreed: Please build the homepage using Shopify’s native Online Store 2.0 sections and blocks (Dawn theme) — no custom code unless absolutely necessary. The goal is a clean, flexible setup that can be maintained and edited later directly within Shopify.
When implementing, please pay particular attention to:
• Design fidelity: spacing, typography, and layout consistent with the Figma mockup.
• Responsiveness: ensure smooth display on desktop, tablet, and mobile.
• Multi-Language: make sure that in the future
• Multi-language: Please also ensure the homepage is structured for future multi-language support — all headings, paragraphs, and buttons should be editable through Shopify’s native text fields
• SEO: follow basic SEO best practices: use a single H1 heading, maintain a clear heading hierarchy (H2/H3), provide alt-text for all images, and keep all textual content indexable by search engines.

Please deliver the work inside a duplicated Shopify theme (e.g., “TinyQuiltHub – Build”), ready for review, along with a short note describing which sections you used and any key settings (image sizes, paddings, or theme tweaks), if not as in Figma described.

```html
<!DOCTYPE html>
<html lang="en">
<head>
<meta charset="utf-8">
<title>TinyQuiltHub – Sewing Holiday Camps for Kids 9-14</title>
<link href="https://fonts.googleapis.com/css2?family=Fredoka:wght@500;600;700&family=Poppins:wght@400;500;600&display=swap" rel="stylesheet">
<style>
:root{
  --blue:#2ea3d6;
  --blue-dark:#1f8fc2;
  --pink:#e3577f;
  --yellow:#f0b81b;
  --navy:#1b2435;
  --ice:#eaf5fb;
  --ink:#262b33;
  --muted:#5d636c;
  --line:#e6e8ec;
  --white:#ffffff;
}
*{box-sizing:border-box;margin:0;padding:0}
html,body{width:1200px;height:4906px;overflow:hidden}
body{position:relative;font-family:"Poppins",sans-serif;color:var(--ink);background:var(--white);font-size:13px}
.abs{position:absolute}
a{color:inherit;text-decoration:none}
.display{font-family:"Fredoka",sans-serif}

/* header */
.site-header{position:absolute;top:0;left:0;width:1200px;height:78px;background:var(--white);z-index:5}
.brand{position:absolute;left:99px;top:0;width:108px;height:110px;background:var(--white);border-radius:0 0 12px 12px;box-shadow:0 6px 18px rgba(0,0,0,.12);display:flex;align-items:center;justify-content:center;font-family:"Poppins",sans-serif;font-weight:600;font-size:14px;color:var(--pink)}
.nav{position:absolute;left:268px;top:30px;display:flex;gap:26px;font-size:12.5px;color:#444}
.nav .active{font-weight:600;color:var(--ink)}
.lang{position:absolute;left:824px;top:30px;font-size:12.5px;color:#444;display:flex;align-items:center;gap:8px}
.btn{display:inline-flex;align-items:center;gap:10px;border-radius:24px;font-size:12.5px;font-weight:500;color:var(--white);padding:0 6px 0 18px;height:40px}
.btn .arrow{width:28px;height:28px;border-radius:50%;background:var(--white);display:flex;align-items:center;justify-content:center}
.btn-pink{background:var(--pink);box-shadow:0 0 0 3px #f7c9d6}
.btn-blue{background:var(--blue);box-shadow:0 0 0 3px #bfe3f3}
.btn-ghost{background:var(--white);color:var(--blue);box-shadow:0 0 0 3px rgba(255,255,255,.45)}
.btn-ghost .arrow{background:var(--blue)}
.header-cta{position:absolute;left:935px;top:20px;height:38px}

/* hero */
.hero{position:absolute;top:78px;left:0;width:1200px;height:550px;background:#f4f4f3;overflow:hidden}
.hero-photo{position:absolute;left:420px;top:0;width:780px;height:550px;background:linear-gradient(100deg,#f4f4f3 0%,#e7e6e4 22%,#d9d6d4 45%,#c8cdd6 70%,#b9c3cf 100%)}
.hero-copy{position:absolute;left:99px;top:78px;width:420px}
.hero h1{font-family:"Fredoka",sans-serif;font-weight:700;font-size:38px;line-height:55px;letter-spacing:.5px}
.c-blue{color:var(--blue)}.c-pink{color:var(--pink)}.c-yellow{color:var(--yellow)}
.hero p{margin-top:18px;font-size:13px;line-height:24px;color:#333;width:380px}
.hero .btn{position:absolute;top:296px;left:0;height:44px}
.happy{position:absolute;top:372px;left:0;display:flex;gap:10px;align-items:center;font-size:13px}
.hero-wave{position:absolute;left:0;bottom:-2px}

/* section labels */
.eyebrow{font-size:13.5px;font-weight:600;color:var(--blue);letter-spacing:.3px;text-transform:uppercase}
.section-title{font-size:26px;font-weight:500;text-transform:uppercase;letter-spacing:.3px;color:var(--ink);position:relative;display:inline-block}
.section-title em{font-style:normal;color:var(--pink);font-weight:600;position:relative}
.section-title em svg{position:absolute;left:-4px;bottom:-8px}
.center{text-align:center;width:1200px;left:0}

/* about */
.about-text{left:600px;top:706px;width:460px}
.about-text .section-title{margin-top:10px}
.about-text p{font-size:12px;line-height:21px;color:#444;margin-top:14px}
.team{display:flex;gap:36px;margin-top:26px}
.member{display:flex;align-items:center;gap:14px}
.avatar{width:66px;height:66px;border-radius:50%;background:radial-gradient(circle at 50% 40%,#d9cfc7,#8a7a70)}
.member strong{display:block;font-size:15px;font-weight:600}
.member span{font-size:12.5px;color:#555}

/* how it works */
.steps{left:141px;top:1419px;display:flex;gap:23px}
.step{width:165px;height:210px;background:var(--white);border-radius:6px;box-shadow:0 6px 18px rgba(40,90,130,.08);padding:16px 14px;position:relative}
.step .num{position:absolute;right:12px;top:8px;font-family:"Fredoka",sans-serif;font-weight:700;font-size:42px;color:#eef0f3}
.step h3{font-size:13.5px;font-weight:500;margin-top:22px}
.step p{font-size:11.5px;line-height:19px;color:#666;margin-top:6px}

/* why */
.feature{font-size:13px;line-height:24px;color:#333;display:flex;align-items:center;gap:18px}
.feature.left{justify-content:flex-end;text-align:right}
.ficon{width:70px;height:70px;border-radius:50%;display:flex;align-items:center;justify-content:center;flex:none}
.bg-yellow{background:var(--yellow)}.bg-blue{background:var(--blue)}.bg-pink{background:var(--pink)}
.ring{left:448px;top:1953px;width:304px;height:304px;border-radius:50%;border:2px dashed #777}
.ring-inner{position:absolute;left:50px;top:50px;width:200px;height:200px;border-radius:50%;background:var(--white);box-shadow:0 8px 30px rgba(0,0,0,.12);display:flex;align-items:center;justify-content:center;font-weight:600;font-size:22px;color:var(--pink)}
.divider{left:141px;top:2347px;width:918px;height:1px;background:var(--line)}

/* camps */
.camps{left:141px;top:2511px;display:flex;gap:36px}
.camp{width:282px;height:375px;border:1px solid var(--line);border-radius:8px;overflow:hidden;background:var(--white);box-shadow:0 4px 14px rgba(0,0,0,.05)}
.camp .img{height:164px}
.camp-body{padding:14px 16px}
.camp h3{font-size:14px;font-weight:500}
.camp p{font-size:11.5px;line-height:20px;color:#666;margin-top:8px;height:82px}
.meta{display:grid;grid-template-columns:1fr 1fr;row-gap:12px;font-size:11.5px;color:#666;margin-top:12px}
.meta b{font-weight:600;color:#222;margin-right:14px}
.meta .r{display:flex;justify-content:space-between}

/* cta */
.cta-band{left:0;top:3040px;width:1200px;height:380px}
.cta{top:3150px}
.cta h2{font-family:"Fredoka",sans-serif;font-weight:700;font-size:38px;color:var(--white);letter-spacing:.5px}
.cta p{font-size:14px;line-height:25px;color:var(--white);margin:14px auto 0;width:620px}

/* faq */
.faq{left:177px;top:3614px;width:846px}
.faq-item{height:62px;background:var(--white);box-shadow:0 4px 14px rgba(0,0,0,.06);border-left:3px solid var(--pink);display:flex;align-items:center;justify-content:space-between;padding:0 22px;font-size:13.5px;font-weight:500;margin-bottom:19px}
.faq-item.open{height:114px;border:1.5px solid var(--pink);border-left:3px solid var(--pink);flex-direction:column;align-items:flex-start;justify-content:center;position:relative}
.faq-item.open p{font-size:11.5px;font-weight:400;line-height:22px;color:#555;margin-top:8px;width:720px}
.faq-item.open svg{position:absolute;right:22px;top:28px}
.to-top{left:1097px;top:4483px;width:42px;height:42px;border-radius:50%;background:var(--pink);display:flex;align-items:center;justify-content:center}

/* footer */
.footer{left:0;top:4552px;width:1200px;height:354px}
.footer-inner{position:absolute;left:0;top:0;width:1200px;height:354px;color:#c9ced8;font-size:12px}
.f-brand{position:absolute;left:147px;top:88px;font-weight:600;font-size:22px;color:var(--pink)}
.follow{position:absolute;left:144px;top:238px;display:flex;align-items:center;gap:8px;font-size:12px;color:#c9ced8}
.soc{width:20px;height:20px;border-radius:50%;border:1.5px solid #c9ced8}
.f-col h4{font-size:14.5px;font-weight:500;color:var(--yellow);margin-bottom:20px}
.f-col li{list-style:none;line-height:29px}
.contact-row{display:flex;align-items:center;gap:14px;margin-bottom:18px;line-height:22px}
.cicon{width:32px;height:32px;border-radius:50%;background:#2c3549;display:flex;align-items:center;justify-content:center;flex:none}
.subscribe{margin-top:16px;width:244px;height:34px;border-radius:18px;background:var(--white);display:flex;align-items:center;justify-content:space-between;padding:0 4px 0 14px;color:#999;font-size:11px}
.subscribe span.go{width:26px;height:26px;border-radius:50%;background:var(--blue);display:flex;align-items:center;justify-content:center}
.copyright{position:absolute;bottom:8px;width:1200px;text-align:center;font-size:11px;color:#c9ced8}
</style>
</head>
<body>

<header class="site-header">
  <a class="brand" href="#">TinyQuiltHub</a>
  <nav class="nav">
    <a class="active" href="#">Home</a><a href="#">About Us</a><a href="#">Camps</a><a href="#">How It Works</a><a href="#">FAQs</a><a href="#">Contact</a>
  </nav>
  <div class="lang">
    <svg width="15" height="15" viewBox="0 0 16 16" fill="none" stroke="#555" stroke-width="1.2"><circle cx="8" cy="8" r="6.5"/><path d="M1.5 8h13M8 1.5c2 2 2 11 0 13M8 1.5c-2 2-2 11 0 13"/></svg>
    English
    <svg width="12" height="12" viewBox="0 0 12 12" fill="none" stroke="#333" stroke-width="1.5"><path d="M2 4l4 4 4-4"/></svg>
  </div>
  <a class="btn btn-pink header-cta" href="#">Contact Us <span class="arrow"><svg width="12" height="12" viewBox="0 0 12 12" fill="none" stroke="#e3577f" stroke-width="1.6"><path d="M3 9l6-6M4 3h5v5"/></svg></span></a>
</header>

<section class="hero">
  <div class="hero-photo" role="img" aria-label="Photo of two children sewing fabric at a sewing machine in a bright studio with clothing racks"></div>
  <div class="hero-copy">
    <h1><span class="c-blue">PREMIUM SEWING</span><br><span class="c-pink">HOLIDAY CAMPS FOR</span><br><span class="c-yellow">KIDS 9-14</span></h1>
    <p>Creative fun in Zurich – Multilingual and Inspiring! Learn sewing, build confidence, and create unique fashion pieces in our small-group camps.</p>
    <a class="btn btn-blue" href="#">View Upcoming Camps <span class="arrow"><svg width="12" height="12" viewBox="0 0 12 12" fill="none" stroke="#2ea3d6" stroke-width="1.6"><path d="M3 9l6-6M4 3h5v5"/></svg></span></a>
    <div class="happy"><svg width="20" height="20" viewBox="0 0 20 20" fill="none" stroke="#333" stroke-width="1.3"><circle cx="10" cy="10" r="8.5"/><path d="M6.5 12c1.8 2 5.2 2 7 0"/><circle cx="7.3" cy="8" r=".8" fill="#333"/><circle cx="12.7" cy="8" r=".8" fill="#333"/></svg>Join 200+ happy campers!</div>
  </div>
  <svg class="hero-wave" width="1200" height="60" viewBox="0 0 1200 60" preserveAspectRatio="none"><path d="M0 22 C180 70 360 0 600 30 S980 5 1200 34 V60 H0Z" fill="#fff"/></svg>
</section>

<!-- about -->
<svg class="abs" style="left:140px;top:700px" width="426" height="428" viewBox="0 0 426 428">
  <defs>
    <clipPath id="disc"><circle cx="213" cy="214" r="210"/></clipPath>
  </defs>
  <g clip-path="url(#disc)">
    <rect role="img" aria-label="Photo of a girl cutting fabric at a craft table" x="48" y="0" width="160" height="209" fill="#d8c7b4"/>
    <path d="M218 4 A210 210 0 0 1 423 209 H218Z" fill="#f0b81b"/>
    <path d="M218 60 A150 150 0 0 1 368 209 H218Z" fill="#e3577f"/>
    <rect role="img" aria-label="Photo of a smiling girl holding fabric" x="0" y="219" width="208" height="209" fill="#cbb9a8"/>
    <rect role="img" aria-label="Photo of a child using a sewing machine" x="218" y="219" width="208" height="209" fill="#b9c0c8"/>
  </g>
  <circle cx="213" cy="214" r="30" fill="#fff" stroke="#f0b81b" stroke-width="3"/>
  <circle cx="213" cy="214" r="20" fill="#eaf5fb"/>
  <path d="M213 224 l-9-9 a5 5 0 0 1 9-6 a5 5 0 0 1 9 6z" fill="#2ea3d6"/>
</svg>

<div class="abs about-text">
  <div class="eyebrow">About Our Camps</div>
  <h2 class="section-title">Learning with fun <em>&amp; Structure<svg width="190" height="10" viewBox="0 0 190 10"><path d="M2 7 C60 1 130 1 188 6" stroke="#e3577f" stroke-width="2" fill="none"/></svg></em></h2>
  <p>At TinyQuiltHub, we believe in nurturing creativity while having fun. Our experienced instructors create a safe, inspiring environment where children can explore their creative potential.</p>
  <p>With over 10 years of experience in teaching children sewing, tailoring, and design, Marlene and Odile guide young talents through a creative week of vacation – with real results: self-sewn pieces, new friends, and lots of pride.</p>
  <p>At the last day, the children show off their success, their own sewn unique pieces, in a sympathetic fashion show.</p>
  <div class="team">
    <div class="member"><div class="avatar" role="img" aria-label="Portrait photo of Marlene"></div><div><strong>Marlene</strong><span>Sewing Expert</span></div></div>
    <div class="member"><div class="avatar" role="img" aria-label="Portrait photo of Odile"></div><div><strong>Odile</strong><span>Design Specialist</span></div></div>
  </div>
</div>

<!-- how it works -->
<svg class="abs" style="left:0;top:1170px" width="1200" height="570" viewBox="0 0 1200 570" preserveAspectRatio="none">
  <path d="M0 30 C200 -10 420 60 640 25 S1000 0 1200 30 V540 C1000 575 760 520 560 548 S160 560 0 535Z" fill="#eaf5fb"/>
</svg>
<div class="abs center" style="top:1328px"><div class="eyebrow">How Our Camps Work</div></div>
<div class="abs center" style="top:1358px"><h2 class="section-title">Creative holiday camps for young <em>Sewing Champs!<svg width="240" height="10" viewBox="0 0 240 10"><path d="M2 7 C80 1 160 1 238 6" stroke="#e3577f" stroke-width="2" fill="none"/></svg></em></h2></div>

<div class="abs steps">
  <div class="step"><span class="num">01</span>
    <svg width="36" height="36" viewBox="0 0 36 36" fill="none" stroke="#e3577f" stroke-width="1.5"><path d="M6 30 L28 8M22 6l8 8M10 22l4 4"/><circle cx="8" cy="28" r="3"/></svg>
    <h3>Project Selection</h3><p>Your child chooses their own model based on previously produced clothing items and sewing patterns.</p></div>
  <div class="step"><span class="num">02</span>
    <svg width="36" height="36" viewBox="0 0 36 36" fill="none" stroke="#e3577f" stroke-width="1.5"><rect x="6" y="10" width="24" height="18" rx="3"/><path d="M6 16h24M6 22h24M12 10V6M24 10V6"/></svg>
    <h3>Fabric selection</h3><p>High-quality fabrics are available.</p></div>
  <div class="step"><span class="num">03</span>
    <svg width="36" height="36" viewBox="0 0 36 36" fill="none" stroke="#e3577f" stroke-width="1.5"><path d="M5 28h26M8 28V10h18v8H14v10"/><path d="M22 18v5"/><circle cx="24" cy="14" r="1.5"/></svg>
    <h3>Sewing machine</h3><p>Learn how to use a sewing machine</p></div>
  <div class="step"><span class="num">04</span>
    <svg width="36" height="36" viewBox="0 0 36 36" fill="none" stroke="#e3577f" stroke-width="1.5"><path d="M8 6h20l-6 12v10l-8 4V18z"/></svg>
    <h3>Sewing &amp; refining</h3><p>Step by step to the goal with professional guidance</p></div>
  <div class="step"><span class="num">05</span>
    <svg width="36" height="36" viewBox="0 0 36 36" fill="none" stroke="#e3577f" stroke-width="1.5"><path d="M12 6l6 4 6-4 6 6-4 4v14H10V16l-4-4z"/></svg>
    <h3>Showtime!</h3><p>Fashion show or photo shoot at the end of the week</p></div>
</div>

<!-- why -->
<div class="abs center" style="top:1837px"><div class="eyebrow">Why Parents Choose Us</div></div>
<div class="abs center" style="top:1866px"><h2 class="section-title">Why families love TinyQuiltHub sewing <em>Camps<svg width="100" height="10" viewBox="0 0 100 10"><path d="M2 7 C30 1 70 1 98 6" stroke="#e3577f" stroke-width="2" fill="none"/></svg></em></h2></div>

<div class="abs ring"><div class="ring-inner">TinyQuiltHub</div></div>

<div class="abs feature left" style="left:120px;top:1946px;width:294px"><span>Small groups &amp;<br>personalized attention</span><span class="ficon bg-yellow"><svg width="30" height="30" viewBox="0 0 30 30" fill="none" stroke="#fff" stroke-width="2.2"><path d="M6 6l8 8M14 8v6H8M24 24l-8-8M16 22v-6h6"/></svg></span></div>
<div class="abs feature left" style="left:90px;top:2070px;width:297px"><span>Multilingual supervision<br>(DE / EN / IT)</span><span class="ficon bg-blue"><svg width="30" height="30" viewBox="0 0 30 30" fill="none" stroke="#fff" stroke-width="2"><path d="M4 8h12M10 5v3M6 8c1 5 4 8 8 10M14 8c-1 5-4 8-8 10M16 26l5-12 5 12M18 22h6"/></svg></span></div>
<div class="abs feature left" style="left:120px;top:2194px;width:294px"><span>Pick-up Service from the<br>Main-Station</span><span class="ficon bg-pink"><svg width="26" height="30" viewBox="0 0 26 30" fill="#fff"><path d="M13 2a9 9 0 0 1 9 9c0 7-9 17-9 17S4 18 4 11a9 9 0 0 1 9-9z"/><circle cx="13" cy="11" r="3.5" fill="#e3577f"/></svg></span></div>

<div class="abs feature" style="left:773px;top:1946px;width:300px"><span class="ficon bg-blue"><svg width="32" height="32" viewBox="0 0 32 32" fill="none" stroke="#fff" stroke-width="2"><path d="M16 4l3.6 7.6 8.2 1-6 5.7 1.5 8.2L16 22.6l-7.3 3.9 1.5-8.2-6-5.7 8.2-1z"/></svg></span><span>Encouragement of creativity,<br>self-confidence, and fine<br>motor skills</span></div>
<div class="abs feature" style="left:798px;top:2070px;width:290px"><span class="ficon bg-pink"><svg width="30" height="30" viewBox="0 0 30 30" fill="none" stroke="#fff" stroke-width="2"><path d="M15 3l10 4v8c0 6-5 10-10 12C10 25 5 21 5 15V7z"/><path d="M10 15l4 4 6-7"/></svg></span><span>Safe, loving environment in<br>Zurich, various places easy<br>to reach</span></div>
<div class="abs feature" style="left:773px;top:2194px;width:300px"><span class="ficon bg-yellow"><svg width="30" height="30" viewBox="0 0 30 30" fill="none" stroke="#fff" stroke-width="1.8"><rect x="5" y="5" width="20" height="20" rx="2"/><path d="M5 11h20M5 17h20M11 5v20M17 5v20"/></svg></span><span>High-quality fabrics &amp; top-<br>quality sewing machines<br>(Stitchwell)</span></div>

<div class="abs divider"></div>

<!-- camps -->
<div class="abs center" style="top:2422px"><div class="eyebrow">Our Upcoming Camps</div></div>
<div class="abs center" style="top:2452px"><h2 class="section-title">Multilingual creativity, made just <em>For Kids<svg width="130" height="10" viewBox="0 0 130 10"><path d="M2 7 C40 1 90 1 128 6" stroke="#e3577f" stroke-width="2" fill="none"/></svg></em></h2></div>

<div class="abs camps">
  <article class="camp"><div class="img" role="img" aria-label="Photo of a woman helping a child with a spring sewing project" style="background:linear-gradient(135deg,#cfd8dc,#a9a19a)"></div>
    <div class="camp-body"><h3>Spring Sewing Camp</h3><p>Join us for a creative week during spring break! Children will learn sewing basics and create their own spring-themed projects.</p>
    <div class="meta"><span><b>Age:</b>09 to 14</span><span class="r"><b>Total:</b>200 Kids</span><span><b>Date:</b>21 Oct,2025</span><span><b>Duration:</b>06 Days</span></div></div></article>
  <article class="camp"><div class="img" role="img" aria-label="Photo of children running across a sunny park lawn" style="background:linear-gradient(135deg,#8fb06b,#506c3a)"></div>
    <div class="camp-body"><h3>Summer Fashion Camp</h3><p>Our popular summer program where kids design and create their own summer wardrobe items in a fun, supportive environment.</p>
    <div class="meta"><span><b>Age:</b>09 to 14</span><span class="r"><b>Total:</b>200 Kids</span><span><b>Date:</b>07 Jul,2025</span><span><b>Duration:</b>06 Days</span></div></div></article>
  <article class="camp"><div class="img" role="img" aria-label="Photo of girls sewing autumn clothing in a workshop" style="background:linear-gradient(135deg,#d6c6b6,#9f8e80)"></div>
    <div class="camp-body"><h3>Autumn Creative Camp</h3><p>Get ready for cooler weather by creating cozy autumn accessories and clothing items in this creative camp Autumn Creative Camp.</p>
    <div class="meta"><span><b>Age:</b>09 to 14</span><span class="r"><b>Total:</b>200 Kids</span><span><b>Date:</b>21 Oct,2025</span><span><b>Duration:</b>06 Days</span></div></div></article>
</div>
<div class="abs center" style="top:2915px"><a class="btn btn-pink" href="#">View All Camps <span class="arrow"><svg width="12" height="12" viewBox="0 0 12 12" fill="none" stroke="#e3577f" stroke-width="1.6"><path d="M3 9l6-6M4 3h5v5"/></svg></span></a></div>

<!-- cta -->
<svg class="abs cta-band" viewBox="0 0 1200 380" preserveAspectRatio="none">
  <path d="M0 30 C220 -10 420 50 640 20 S1000 -5 1200 30 V350 C980 390 760 330 560 360 S180 370 0 345Z" fill="#2ea3d6"/>
</svg>
<div class="abs center cta">
  <h2>READY FOR A CREATIVE ADVENTURE?</h2>
  <p>Spaces are limited to 8 children per camp to ensure personalized attention. Book now to secure your child's spot!</p>
  <a class="btn btn-ghost" style="margin-top:22px" href="#">View All Camps <span class="arrow"><svg width="12" height="12" viewBox="0 0 12 12" fill="none" stroke="#fff" stroke-width="1.6"><path d="M3 9l6-6M4 3h5v5"/></svg></span></a>
</div>

<!-- faq -->
<div class="abs center" style="top:3527px"><div class="eyebrow" style="color:#e3577f">Frequently Asked Questions</div></div>
<div class="abs center" style="top:3557px"><h2 class="section-title">Everything you need to know about <em>Our Camps<svg width="160" height="10" viewBox="0 0 160 10"><path d="M2 7 C50 1 110 1 158 6" stroke="#e3577f" stroke-width="2" fill="none"/></svg></em></h2></div>

<div class="abs faq">
  <div class="faq-item open">Does my child need any prior knowledge?
    <p>We welcome children aged 9-14 years. This age range ensures that participants have the fine motor skills needed for sewing while still being excited about creative projects.</p>
    <svg width="14" height="14" viewBox="0 0 14 14" fill="none" stroke="#333" stroke-width="1.6"><path d="M2 9l5-5 5 5"/></svg></div>
  <div class="faq-item">How does the pick-up service work?<svg width="14" height="14" viewBox="0 0 14 14" fill="none" stroke="#333" stroke-width="1.6"><path d="M2 5l5 5 5-5"/></svg></div>
  <div class="faq-item">How many items of clothing are produced?<svg width="14" height="14" viewBox="0 0 14 14" fill="none" stroke="#333" stroke-width="1.6"><path d="M2 5l5 5 5-5"/></svg></div>
  <div class="faq-item">What should my child bring to camp?<svg width="14" height="14" viewBox="0 0 14 14" fill="none" stroke="#333" stroke-width="1.6"><path d="M2 5l5 5 5-5"/></svg></div>
  <div class="faq-item">What are the camp hours?<svg width="14" height="14" viewBox="0 0 14 14" fill="none" stroke="#333" stroke-width="1.6"><path d="M2 5l5 5 5-5"/></svg></div>
  <div class="faq-item">We offer pick-up from Zurich Main Station at times. Parents can arrange this during booking<svg width="14" height="14" viewBox="0 0 14 14" fill="none" stroke="#333" stroke-width="1.6"><path d="M2 5l5 5 5-5"/></svg></div>
  <div class="faq-item">What is your cancellation policy?<svg width="14" height="14" viewBox="0 0 14 14" fill="none" stroke="#333" stroke-width="1.6"><path d="M2 5l5 5 5-5"/></svg></div>
  <div class="faq-item">How many items of clothing are produced?<svg width="14" height="14" viewBox="0 0 14 14" fill="none" stroke="#333" stroke-width="1.6"><path d="M2 5l5 5 5-5"/></svg></div>
  <div class="faq-item">Each child completes their own unique clothing item during the week<svg width="14" height="14" viewBox="0 0 14 14" fill="none" stroke="#333" stroke-width="1.6"><path d="M2 5l5 5 5-5"/></svg></div>
  <div class="faq-item">What safety measures are in place?<svg width="14" height="14" viewBox="0 0 14 14" fill="none" stroke="#333" stroke-width="1.6"><path d="M2 5l5 5 5-5"/></svg></div>
</div>
<a class="abs to-top" href="#" aria-label="Back to top"><svg width="18" height="18" viewBox="0 0 18 18" fill="none" stroke="#fff" stroke-width="2.2"><path d="M4 10l5-5 5 5M4 15l5-5 5 5"/></svg></a>

<!-- footer -->
<footer class="abs footer">
  <svg class="abs" style="left:0;top:0" width="1200" height="354" viewBox="0 0 1200 354" preserveAspectRatio="none"><path d="M0 22 C200 -4 420 30 640 12 S1000 0 1200 24 V354 H0Z" fill="#1b2435"/></svg>
  <div class="footer-inner">
    <div class="f-brand">TinyQuiltHub</div>
    <div class="follow">Follow Us: <span class="soc" aria-label="Social profile 1"></span><span class="soc" aria-label="Social profile 2"></span><span class="soc" aria-label="Social profile 3"></span></div>
    <div class="abs f-col" style="left:364px;top:92px"><h4>Quick Links</h4><ul><li>Home</li><li>About Us</li><li>Camps</li><li>How It Works</li><li>Contact</li></ul></div>
    <div class="abs f-col" style="left:516px;top:92px;width:260px"><h4>Contact Us</h4>
      <div class="contact-row"><span class="cicon"><svg width="12" height="14" viewBox="0 0 12 14" fill="#c9ced8"><path d="M6 0a5 5 0 0 1 5 5c0 4-5 9-5 9S1 9 1 5a5 5 0 0 1 5-5z"/><circle cx="6" cy="5" r="2" fill="#2c3549"/></svg></span><span>B-47, Lindenweg 12, 8001<br>Zurich, Switzerland</span></div>
      <div class="contact-row"><span class="cicon" style="background:var(--blue)"><svg width="14" height="14" viewBox="0 0 14 14" fill="#fff"><path d="M3 1l2.5 3-1.5 1.5c.8 1.8 2.2 3.2 4 4L9.5 8 13 10.5 11.5 13C6 13 1 8 1 2.5z"/></svg></span><span>Phone: (555)-018 2294</span></div>
      <div class="contact-row"><span class="cicon"><svg width="14" height="12" viewBox="0 0 14 12" fill="none" stroke="#c9ced8" stroke-width="1.4"><rect x="1" y="1" width="12" height="10" rx="1"/><path d="M1 2l6 5 6-5"/></svg></span><span>hello@tinyquilthub.com</span></div>
    </div>
    <div class="abs f-col" style="left:812px;top:92px;width:260px"><h4>Subscribe to newsletter</h4>
      <p style="line-height:22px">latest updates, exclusive content, and special offers? Subscribe to our newsletter!</p>
      <div class="subscribe"><span>✉ Your Email</span><span class="go"><svg width="12" height="12" viewBox="0 0 12 12" fill="none" stroke="#fff" stroke-width="1.8"><path d="M2 6h8M7 3l3 3-3 3"/></svg></span></div>
    </div>
    <div class="copyright">© 2025 TinyQuiltHub. All Rights Reserved.</div>
  </div>
</footer>

</body>
</html>
```